Business Landing Page for SEO Company

Need the landing page of the website designed - I will provide the copy, will need to include details of my company and the services offered, about us, testimonials, faq, etc., and all these elements will need to be arranged graphically on the page.

I want something similar to this: https://pebrovault.com/

Not in terms of color or theme or anything, but we offer a similar service and want to display similar information.

Th services we provide are:

Premium Links
Monthly Links Subscription
Link Insertions

Need to advertise them on the front page. Additionally need a place for testimonials, company details, etc.,

We already have logo for the website. Please use the attached file to insert the logo within the overal design.

Target Market(s)

SEO marketers and agencies

Number of Pages Required

1 page

```html
<!DOCTYPE html>
<html lang="en">
<head>
<meta charset="utf-8">
<title>Linkora – Link Building for SEO Marketers and Agencies</title>
<link rel="stylesheet" href="https://fonts.googleapis.com/css2?family=Nunito:wght@400;600;700&display=swap">
<style>
:root{
  --blue:#2b7fd4;
  --navy:#1d3a5c;
  --orange:#ff7a00;
  --text:#3d4a5a;
  --muted:#6b7684;
  --line:#dfe4ea;
  --soft:#f2f4f7;
  --white:#ffffff;
}
*{margin:0;padding:0;box-sizing:border-box}
html,body{width:1200px;height:2877px;overflow:hidden;background:var(--white)}
body{font-family:"Nunito",sans-serif;color:var(--text);position:relative;letter-spacing:.04em}
.abs{position:absolute}
.center{left:0;width:1200px;text-align:center}

/* nav */
.site-nav{top:0;left:0;width:1200px;height:62px;border-bottom:1px solid var(--line)}
.brand{left:225px;top:12px;font-size:28px;font-weight:700;color:var(--blue);letter-spacing:0;display:flex;align-items:center;gap:6px}
.brand-dot{width:8px;height:8px;background:var(--blue);border-radius:50%}
.menu{left:382px;top:22px;display:flex;gap:27px;font-size:11px;letter-spacing:.08em}
.menu a{color:var(--navy);text-decoration:none}
.menu a.active{color:var(--orange)}
.btn-outline{left:789px;top:14px;width:185px;height:28px;border:1px solid var(--navy);border-radius:3px;font-size:12px;color:var(--navy);font-weight:600;display:flex;align-items:center;justify-content:center;letter-spacing:0}

/* hero */
.hero-title{top:130px;font-size:25px;line-height:32px;color:var(--blue);font-weight:400;letter-spacing:.08em}
.lead{font-size:12px;line-height:16px;color:var(--text)}
.btn{height:25px;border-radius:3px;font-size:12px;color:var(--white);display:flex;align-items:center;justify-content:center;gap:5px;letter-spacing:0;box-shadow:0 3px 6px rgba(0,0,0,.15)}
.btn-orange{background:var(--orange)}
.btn-navy{background:var(--navy)}
.watch{display:flex;align-items:center;gap:14px;font-size:11px;color:var(--navy);letter-spacing:.08em}
.play{width:25px;height:25px;border-radius:50%;background:var(--navy);display:flex;align-items:center;justify-content:center}

/* trusted */
.eyebrow{font-size:11px;color:var(--navy);letter-spacing:.14em;font-weight:600}
.partners{top:451px;left:225px;width:749px;height:63px;border-top:1px solid #c9d3de;border-bottom:1px solid #c9d3de;display:flex;justify-content:space-between;align-items:center}
.partner{font-size:17px;color:#8a939e;font-weight:600;letter-spacing:0}

/* services */
.service{width:220px;text-align:center}
.service-icon{width:74px;height:74px;border-radius:50%;margin:0 auto;background:linear-gradient(135deg,#ffffff,#eceff3);box-shadow:4px 4px 10px rgba(0,0,0,.06);display:flex;align-items:center;justify-content:center}
.service h3{font-size:15px;font-weight:400;color:#1f2a37;margin-top:18px;line-height:20px;height:40px}
.service p{font-size:11px;line-height:16px;color:var(--muted);margin-top:24px}

.section-title{font-size:21px;font-weight:400;color:#1f2a37;letter-spacing:.08em}

/* testimonials */
.t-card{top:1061px;width:235px;height:177px;border:1px solid var(--line);border-radius:4px;text-align:center}
.avatar{position:absolute;left:50%;top:-34px;margin-left:-33px;width:66px;height:66px;border-radius:50%;background:radial-gradient(circle at 50% 40%,#8a7c72,#2f2a28)}
.stars{margin-top:40px;display:flex;justify-content:center;gap:11px}
.t-card p{font-size:11px;line-height:15px;color:var(--muted);margin:12px 20px 0}
.t-name{font-size:12px;color:var(--blue);margin-top:17px}
.dots{top:1252px;left:568px;display:flex;gap:13px}
.dots span{width:12px;height:12px;border-radius:50%;background:#b8c2cc}
.dots span:first-child{background:#4d5f76}

/* about */
.about-photo{left:226px;top:1366px;width:236px;height:321px;border-radius:40px 0 0 0;background:linear-gradient(160deg,#8c7d70 0%,#c8b8a6 40%,#b8673a 75%,#d7b08a 100%)}
.about-title{left:562px;top:1446px;font-size:23px;line-height:30px;color:var(--blue);letter-spacing:.08em}
.about-title b{font-weight:600}
.about-text{left:562px;top:1516px;width:370px;font-size:11px;line-height:16px;color:var(--muted)}
.quote-mark{left:938px;top:1398px;width:24px;height:108px}

/* case studies */
.case{top:1877px;width:237px;height:212px;border:1px solid var(--line);border-radius:4px;overflow:hidden}
.case-photo{height:125px}
.case h4{font-size:12px;font-weight:400;color:#1f2a37;line-height:16px;margin:20px 30px 0}
.case-link{font-size:11px;color:var(--blue);margin:12px 30px 0;display:flex;align-items:center;gap:6px}

/* faq */
.faq{width:360px}
.faq h5{font-size:12px;font-weight:600;color:#1f2a37}
.faq p{font-size:11px;line-height:15px;color:var(--muted);margin-top:19px}

/* cta */
.cta-band{top:2536px;left:0;width:1200px;height:256px;background:linear-gradient(180deg,#ffffff 0%,#e9e6e2 30%,#cfc8bf 70%,#a9a199 100%)}
.cta-title{top:2600px;font-size:22px;color:var(--blue);letter-spacing:.08em}

/* footer */
.site-footer{top:2792px;left:0;width:1200px;height:85px;background:var(--navy)}
.socials{top:2816px;left:507px;display:flex;gap:30px}
.socials span{width:14px;height:14px;border-radius:50%;background:#c9d3de}
.copyright{top:2848px;font-size:11px;color:#aab6c4}
</style>
</head>
<body>

<header class="site-nav abs">
  <div class="brand abs"><span class="brand-dot"></span>Linkora</div>
  <nav class="menu abs">
    <a class="active" href="#">HOME</a><a href="#">SERVICES</a><a href="#">CASE STUDIES</a><a href="#">ABOUT US</a><a href="#">FAQ</a>
  </nav>
  <div class="btn-outline abs">Schedule A Free Consultation</div>
</header>

<section class="hero">
  <h1 class="hero-title abs center">The Best Building Link Service Made For<br>SEO Marketers And Agencies</h1>
  <p class="lead abs center" style="top:208px">Lorem Ipsum Dolor Sit Amet Consectetur Adipiscing Elit Nulla Imperdiet Urna Lectus Id<br>Pellentesque Ipsum Bibendum Quis.</p>
  <div class="btn btn-orange abs" style="left:466px;top:296px;width:108px">Our Services
    <svg width="6" height="9" viewBox="0 0 6 9"><path d="M1 1l3.5 3.5L1 8" stroke="#fff" stroke-width="1.4" fill="none"/></svg></div>
  <div class="watch abs" style="left:616px;top:296px"><span class="play"><svg width="9" height="10" viewBox="0 0 9 10"><path d="M1 0l8 5-8 5z" fill="#fff"/></svg></span>WATCH VIDEO</div>
</section>

<section class="trusted">
  <p class="eyebrow abs center" style="top:413px">TRUSTED BY</p>
  <div class="partners abs">
    <span class="partner">Norvio</span><span class="partner">Kestrel</span><span class="partner">Plumtide</span><span class="partner">Veyra Pay</span><span class="partner">Stride</span><span class="partner">Halcom</span>
  </div>
</section>

<section class="services">
  <div class="service abs" style="left:234px;top:590px">
    <div class="service-icon"><svg width="32" height="28" viewBox="0 0 32 28"><path d="M2 9l6-7h16l6 7-14 17z M2 9h28 M10 9l6 17 6-17 M8 2l2 7 6-7 6 7 2-7" fill="none" stroke="#1d4f8f" stroke-width="2" stroke-linejoin="round"/></svg></div>
    <h3>Premium Links</h3>
    <p>Lorem Ipsum Dolor Sit Amet Consectetur Adipiscing Elit. Donec In Eros.</p>
  </div>
  <div class="service abs" style="left:489px;top:590px">
    <div class="service-icon"><svg width="30" height="30" viewBox="0 0 30 30"><rect x="2" y="5" width="26" height="23" rx="2" fill="none" stroke="#1d4f8f" stroke-width="2"/><path d="M2 11h26 M9 2v6 M21 2v6" stroke="#1d4f8f" stroke-width="2"/><path d="M7 16h4 M13 16h4 M19 16h4 M7 21h4 M13 21h4 M19 21h4" stroke="#1d4f8f" stroke-width="2"/></svg></div>
    <h3>Monthly Links<br>Subscription</h3>
    <p>Lorem Ipsum Dolor Sit Amet Consectetur Adipiscing Elit. Donec In Eros.</p>
  </div>
  <div class="service abs" style="left:746px;top:590px">
    <div class="service-icon"><svg width="30" height="30" viewBox="0 0 30 30"><rect x="7" y="2" width="21" height="21" rx="3" fill="none" stroke="#1d4f8f" stroke-width="2"/><path d="M3 7v18a2 2 0 002 2h18" fill="none" stroke="#1d4f8f" stroke-width="2"/><path d="M14 16l7-7 M13 12l-2 2a2.5 2.5 0 003.5 3.5l2-2 M18 13l2-2a2.5 2.5 0 00-3.5-3.5l-2 2" fill="none" stroke="#1d4f8f" stroke-width="1.8"/></svg></div>
    <h3>Link Insertions</h3>
    <p>Lorem Ipsum Dolor Sit Amet Consectetur Adipiscing Elit. Donec In Eros.</p>
  </div>
</section>

<section class="testimonials">
  <h2 class="section-title abs center" style="top:886px">What Our Customers Say</h2>
  <p class="lead abs center" style="top:928px;color:var(--muted);font-size:11px">Lorem Ipsum Dolor Sit Amet Consectetur Adipiscing Elit Cras Lobortis<br>Semper Sagittis Proin Ullamcorper Nunc Ac Accumsan.</p>

  <article class="t-card abs" style="left:227px">
    <div class="avatar" role="img" aria-label="Portrait of the customer"></div>
    <div class="stars"><svg width="108" height="14" viewBox="0 0 108 14"><g fill="#ff7a00"><path id="st" d="M7 0l2 4.7 5 .4-3.8 3.3 1.2 5L7 10.8 2.6 13.4l1.2-5L0 5.1l5-.4z"/><use href="#st" x="26"/><use href="#st" x="52"/><use href="#st" x="78"/><use href="#st" x="94" transform="translate(10 0)"/></g></svg></div>
    <p>Lorem Ipsum Dolor Sit Amet Consectetur Adipiscing Elit Etiam Mollis Sollicitudin Felis.</p>
    <div class="t-name">Mara T. Olsen | CEO</div>
  </article>
  <article class="t-card abs" style="left:482px">
    <div class="avatar" role="img" aria-label="Portrait of the customer"></div>
    <div class="stars"><svg width="108" height="14" viewBox="0 0 108 14"><g fill="#ff7a00"><use href="#st"/><use href="#st" x="26"/><use href="#st" x="52"/><use href="#st" x="78"/><use href="#st" x="104" transform="translate(0 0)"/></g></svg></div>
    <p>Lorem Ipsum Dolor Sit Amet Consectetur Adipiscing Elit Etiam Mollis Sollicitudin Felis.</p>
    <div class="t-name">Dina K. Rowe | Manager</div>
  </article>
  <article class="t-card abs" style="left:739px">
    <div class="avatar" role="img" aria-label="Portrait of the customer" style="background:radial-gradient(circle at 50% 40%,#e8c98a,#8a8f96)"></div>
    <div class="stars"><svg width="108" height="14" viewBox="0 0 108 14"><g fill="#ff7a00"><use href="#st"/><use href="#st" x="26"/><use href="#st" x="52"/><use href="#st" x="78"/><use href="#st" x="104"/></g></svg></div>
    <p>Lorem Ipsum Dolor Sit Amet Consectetur Adipiscing Elit Etiam Mollis Sollicitudin Felis.</p>
    <div class="t-name">Tessa L. Grant | Analyst</div>
  </article>
  <div class="dots abs"><span></span><span></span><span></span></div>
</section>

<section class="about">
  <div class="about-photo abs" role="img" aria-label="Team working together in an office with orange chairs"></div>
  <svg class="quote-mark abs" viewBox="0 0 24 108"><rect x="0" y="0" width="22" height="20" fill="#fcd9b4"/><path d="M2 64h22v14c0 10-6 18-18 22l-2-5c6-3 9-7 9-12H2z" fill="#fcd9b4"/></svg>
  <h2 class="about-title abs">We Are An Agency Specialized<br>In <b>Building Link Service</b></h2>
  <p class="about-text abs">Lorem Ipsum Dolor Sit Amet Consectetur Adipiscing Elit Vestibulum Volutpat Lacus In Nunc Bibendum Id Mattis Libero Vulputate.</p>
  <div class="btn btn-navy abs" style="left:562px;top:1589px;width:100px">Learn More
    <svg width="6" height="9" viewBox="0 0 6 9"><path d="M1 1l3.5 3.5L1 8" stroke="#fff" stroke-width="1.4" fill="none"/></svg></div>
  <div class="watch abs" style="left:705px;top:1589px"><span class="play" style="background:#3a3f46"><svg width="9" height="10" viewBox="0 0 9 10"><path d="M1 0l8 5-8 5z" fill="#fff"/></svg></span>WATCH VIDEO</div>
</section>

<section class="case-studies">
  <h2 class="section-title abs center" style="top:1748px">Case Studies</h2>
  <p class="lead abs center" style="top:1790px;color:var(--muted);font-size:11px">Lorem Ipsum Dolor Sit Amet Consectetur Adipiscing Elit Nam Suscipit Vitae<br>Neque Id Lacinia Cras Mollis Egestas.</p>

  <article class="case abs" style="left:225px">
    <div class="case-photo" role="img" aria-label="Open office with brick wall and desks" style="background:linear-gradient(120deg,#3c4148,#a56a52 50%,#e4e1dc)"></div>
    <h4>Lorem Ipsum Dolor Sit Amet Consectetur</h4>
    <div class="case-link">Lern More <svg width="6" height="9" viewBox="0 0 6 9"><path d="M1 1l3.5 3.5L1 8" stroke="#2b7fd4" stroke-width="1.4" fill="none"/></svg></div>
  </article>
  <article class="case abs" style="left:481px">
    <div class="case-photo" role="img" aria-label="Team meeting around a table in a bright office" style="background:linear-gradient(180deg,#eef0f1,#b9b4ae 60%,#6a5a52)"></div>
    <h4>Lorem Ipsum Dolor Sit Amet Consectetur</h4>
    <div class="case-link">Lern More <svg width="6" height="9" viewBox="0 0 6 9"><path d="M1 1l3.5 3.5L1 8" stroke="#2b7fd4" stroke-width="1.4" fill="none"/></svg></div>
  </article>
  <article class="case abs" style="left:737px">
    <div class="case-photo" role="img" aria-label="Presentation at a whiteboard in a loft office" style="background:linear-gradient(180deg,#e6e9ec,#a8a6a2 55%,#4b4540)"></div>
    <h4>Lorem Ipsum Dolor Sit Amet Consectetur</h4>
    <div class="case-link">Lern More <svg width="6" height="9" viewBox="0 0 6 9"><path d="M1 1l3.5 3.5L1 8" stroke="#2b7fd4" stroke-width="1.4" fill="none"/></svg></div>
  </article>
  <div class="btn btn-navy abs" style="left:550px;top:2128px;width:100px">Learn More
    <svg width="6" height="9" viewBox="0 0 6 9"><path d="M1 1l3.5 3.5L1 8" stroke="#fff" stroke-width="1.4" fill="none"/></svg></div>
</section>

<section class="faq-section">
  <h2 class="section-title abs center" style="top:2236px;color:var(--blue)">FAQ</h2>
  <div class="faq abs" style="left:225px;top:2293px"><h5>Lorem Ipsum Dolor It Consectetur?</h5><p>Lorem Ipsum Dolor Sit Amet Consectetur Adipiscing Elit Nunc Et Consectetur Libero Placerat Posuere.</p></div>
  <div class="faq abs" style="left:612px;top:2293px"><h5>Lorem Ipsum Dolor It Consectetur?</h5><p>Lorem Ipsum Dolor Sit Amet Consectetur Adipiscing Elit Nunc Et Consectetur Libero Placerat Posuere.</p></div>
  <div class="faq abs" style="left:225px;top:2414px"><h5>Lorem Ipsum Dolor It Consectetur?</h5><p>Lorem Ipsum Dolor Sit Amet Consectetur Adipiscing Elit Nunc Et Consectetur Libero Placerat Posuere.</p></div>
  <div class="faq abs" style="left:612px;top:2414px"><h5>Lorem Ipsum Dolor It Consectetur?</h5><p>Lorem Ipsum Dolor Sit Amet Consectetur Adipiscing Elit Nunc Et Consectetur Libero Placerat Posuere.</p></div>
</section>

<section class="cta">
  <div class="cta-band abs" role="img" aria-label="Faded photo of a team working on laptops"></div>
  <h2 class="cta-title abs center">Get The Best Building Link Service</h2>
  <p class="lead abs center" style="top:2641px;font-size:11px">Lorem Ipsum Dolor Sit Amet Consectetur Adipiscing Elit Fusce Et Lorem Eu<br>Odio Rhoncus Eleifend Sed In.</p>
  <div class="btn abs" style="left:551px;top:2686px;width:98px;background:#8fa0b3;box-shadow:none;color:var(--navy)">Contact Us
    <svg width="6" height="9" viewBox="0 0 6 9"><path d="M1 1l3.5 3.5L1 8" stroke="#1d3a5c" stroke-width="1.4" fill="none"/></svg></div>
</section>

<footer class="site-footer abs"></footer>
<div class="socials abs"><span></span><span></span><span></span><span></span><span></span></div>
<p class="copyright abs center">© 2021 Linkora. All Rights Reserved.</p>

</body>
</html>
```